Business Card Design for The Lending Nook Inc.

We need a business card design for our mortgage company: "The Lending Nook Inc."

Need to have Social Media Account on there as a possibility

Industry/Entity Type

Business

```html
<!DOCTYPE html>
<html lang="en">
<head>
<meta charset="UTF-8">
<title>The Lending Nook Inc. — Business Card</title>
<link rel="stylesheet" href="https://fonts.googleapis.com/css2?family=Arimo:wght@400;700&display=swap">
<style>
  :root {
    --page-bg: #e4e2df;
    --card-white: #ffffff;
    --strip-grey: #ececef;
    --brand-blue: #1f5fb4;
    --ink-dark: #2a2a2c;
    --ink-body: #3b3b3e;
    --ink-muted: #8a8a90;
    --edge-shadow: rgba(0, 0, 0, 0.18);
  }
  * { box-sizing: border-box; margin: 0; padding: 0; }
  html, body {
    width: 1200px; height: 800px; overflow: hidden;
    background: var(--page-bg);
    font-family: "Arimo", Arial, sans-serif;
  }
  .canvas {
    position: relative; width: 1200px; height: 800px;
    display: flex; align-items: center; justify-content: center; gap: 60px;
  }
  .card {
    position: relative; width: 520px; height: 300px;
    background: var(--card-white);
    box-shadow: 0 10px 26px var(--edge-shadow);
    overflow: hidden;
  }

  /* Front */
  .front-banner {
    position: absolute; left: 30px; top: 70px; width: 440px; height: 110px;
    filter: drop-shadow(0 3px 4px rgba(0,0,0,0.22));
  }
  .front-banner svg { position: absolute; inset: 0; }
  .brand-lockup {
    position: absolute; inset: 0;
    display: flex; align-items: center; gap: 16px; padding-left: 44px;
  }
  .brand-dot {
    width: 46px; height: 46px; border-radius: 50%;
    border: 4px solid var(--brand-blue); flex: none;
  }
  .brand-name {
    color: var(--brand-blue); font-weight: 700; font-size: 34px; letter-spacing: -0.5px;
  }
  .front-website {
    position: absolute; left: 0; right: 0; top: 214px;
    text-align: center; font-size: 15px; letter-spacing: 3px; color: var(--ink-muted);
  }

  /* Back */
  .back-strip {
    position: absolute; left: 0; top: 0; bottom: 0; width: 170px;
    background: var(--strip-grey);
  }
  .strip-lockup {
    position: absolute; left: 85px; top: 150px;
    transform: translate(-50%, -50%) rotate(-90deg);
    display: flex; align-items: center; gap: 10px; white-space: nowrap;
  }
  .strip-dot {
    width: 30px; height: 30px; border-radius: 50%;
    border: 3px solid var(--ink-muted); flex: none;
  }
  .strip-name { color: var(--ink-muted); font-weight: 700; font-size: 21px; }
  .corner-mark { position: absolute; }
  .corner-top { left: 200px; top: 40px; }
  .corner-bottom { right: 24px; bottom: 24px; }
  .person-name {
    position: absolute; left: 248px; top: 48px;
    font-weight: 700; font-size: 25px; line-height: 1.05; letter-spacing: 1px;
    color: var(--ink-dark); text-transform: uppercase;
  }
  .contact-list {
    position: absolute; left: 206px; top: 140px; list-style: none;
    display: flex; flex-direction: column; gap: 12px;
  }
  .contact-item {
    display: flex; align-items: center; gap: 14px;
    font-size: 14px; color: var(--ink-body);
  }
  .contact-icon { width: 16px; height: 16px; flex: none; }
</style>
</head>
<body>
<main class="canvas">

  <section class="card card-front" aria-label="Card front">
    <div class="front-banner">
      <svg viewBox="0 0 440 110" width="440" height="110" aria-hidden="true">
        <polygon points="22,0 440,0 440,80 410,110 0,110 0,22" fill="var(--card-white)"/>
      </svg>
      <div class="brand-lockup">
        <span class="brand-dot"></span>
        <span class="brand-name">The Lending Nook Inc.</span>
      </div>
    </div>
    <p class="front-website">WWW.LENDINGNOOK.COM</p>
  </section>

  <section class="card card-back" aria-label="Card back">
    <div class="back-strip">
      <div class="strip-lockup">
        <span class="strip-dot"></span>
        <span class="strip-name">The Lending Nook Inc.</span>
      </div>
    </div>

    <svg class="corner-mark corner-top" width="34" height="22" viewBox="0 0 34 22" aria-hidden="true">
      <polygon points="0,0 34,0 0,22" fill="var(--brand-blue)"/>
    </svg>

    <h1 class="person-name">Daniel<br>Carter</h1>

    <ul class="contact-list">
      <li class="contact-item">
        <svg class="contact-icon" viewBox="0 0 16 16" aria-hidden="true">
          <path d="M8 1.5a4.5 4.5 0 0 0-4.5 4.5c0 3.4 4.5 8.5 4.5 8.5s4.5-5.1 4.5-8.5A4.5 4.5 0 0 0 8 1.5z" fill="none" stroke="var(--ink-body)" stroke-width="1.3"/>
          <circle cx="8" cy="6" r="1.6" fill="var(--ink-body)"/>
        </svg>
        <span>Adress Line Here</span>
      </li>
      <li class="contact-item">
        <svg class="contact-icon" viewBox="0 0 16 16" aria-hidden="true">
          <path d="M4 1.5l2.5 3-1.5 1.8c.8 1.8 2 3 3.8 3.8l1.8-1.5 3 2.5-1.6 2.4C7.5 13.5 2.5 8.5 1.6 3.1z" fill="var(--ink-body)"/>
        </svg>
        <span>+ 0 123 480 915</span>
      </li>
      <li class="contact-item">
        <svg class="contact-icon" viewBox="0 0 16 16" aria-hidden="true">
          <rect x="1.5" y="3.5" width="13" height="9" fill="none" stroke="var(--ink-body)" stroke-width="1.3"/>
          <polyline points="1.5,3.5 8,9 14.5,3.5" fill="none" stroke="var(--ink-body)" stroke-width="1.3"/>
        </svg>
        <span>danielcarter@mail.com</span>
      </li>
      <li class="contact-item">
        <svg class="contact-icon" viewBox="0 0 16 16" aria-hidden="true">
          <circle cx="8" cy="8" r="6.5" fill="none" stroke="var(--ink-body)" stroke-width="1.3"/>
          <ellipse cx="8" cy="8" rx="2.8" ry="6.5" fill="none" stroke="var(--ink-body)" stroke-width="1.1"/>
          <line x1="1.5" y1="8" x2="14.5" y2="8" stroke="var(--ink-body)" stroke-width="1.1"/>
        </svg>
        <span>www.lendingnook.com</span>
      </li>
    </ul>

    <svg class="corner-mark corner-bottom" width="34" height="22" viewBox="0 0 34 22" aria-hidden="true">
      <polygon points="34,0 34,22 0,22" fill="var(--brand-blue)"/>
    </svg>
  </section>

</main>
</body>
</html>
```